WordPress Site That Reviews Footwear

We need a wordpress web design for an affiliate site called TarnWisp. We review and do roundups on footwear products. The final design should be clean and mobile friendly. The site should be built with Gutenberg page builder. We like the design of https://petalharvin.com/.

Target Market(s)

USA

Industry/Entity Type

Footwear

Logo Text

TarnWisp

Number of Pages Required

4 page

Font styles to use
Serif
Sans Serif

Requirements
Must have
• Wordpress site
Blog post
Page
Categories
Homepage

```html
<!DOCTYPE html>
<html lang="en">
<head>
<meta charset="utf-8">
<title>TarnWisp — Footwear Reviews</title>
<link href="https://fonts.googleapis.com/css2?family=Noto+Serif:wght@700&family=Roboto:wght@400;500;700&display=swap" rel="stylesheet">
<style>
:root{
  --yellow:#f5b000;
  --ink:#111111;
  --grey:#6f6f6f;
  --muted:#8a8a8a;
  --soft:#f2f2f2;
  --blog:#3f6579;
  --footer:#000000;
  --white:#ffffff;
  --serif:'Noto Serif', Georgia, serif;
  --sans:'Roboto', Arial, sans-serif;
}
*{margin:0;padding:0;box-sizing:border-box}
html,body{width:1200px;height:3019px;overflow:hidden}
body{position:relative;font-family:var(--sans);color:var(--ink);background:var(--white)}
.abs{position:absolute}
.topbar{left:0;top:0;width:1200px;height:5px;background:var(--yellow)}
.nav{left:0;top:5px;width:1200px;height:85px}
.nav a{position:absolute;top:36px;font-size:15px;color:var(--ink);text-decoration:none;text-transform:uppercase}
.brand{font-family:var(--serif);font-weight:700;color:var(--ink)}
.nav .brand{position:absolute;left:464px;top:20px;font-size:40px;letter-spacing:.5px}
.nav .social{position:absolute;top:41px;width:11px;height:11px;border-radius:50%;background:var(--ink)}
.hero{left:0;top:90px;width:1200px;height:542px;background:linear-gradient(100deg,#7a4a2c 0%,#a0603a 40%,#6b3c24 75%,#3b2418 100%)}
.hero-title{left:736px;top:252px;font-family:var(--serif);font-weight:700;font-size:62px;color:var(--white)}
.hero-text{left:736px;top:338px;width:380px;font-size:16px;line-height:22px;color:var(--white)}
.btn{display:flex;align-items:center;gap:12px;justify-content:center;background:var(--yellow);color:var(--ink);font-weight:500;font-size:16px;text-transform:uppercase;border-radius:2px}
.btn svg{width:15px;height:15px}
.slider-btn{width:35px;height:26px;border-radius:3px;display:flex;align-items:center;justify-content:center}
.h2{font-family:var(--serif);font-weight:700;font-size:40px;color:var(--ink);text-transform:uppercase}
.rule{height:3px;width:37px;background:var(--yellow)}
.body-grey{font-size:16px;line-height:26px;color:var(--grey);font-weight:500}
.card{width:170px;height:123px;background:var(--white);border:1px solid #ececec;box-shadow:0 2px 6px rgba(0,0,0,.06);border-radius:3px;text-align:center}
.card svg{position:absolute;left:50%;top:14px;transform:translateX(-50%)}
.card span{position:absolute;left:0;right:0;top:90px;font-size:15px;font-weight:500;color:var(--ink)}
.card.active{border-bottom:4px solid var(--yellow)}
.about{left:0;top:1093px;width:1200px;height:460px;background:var(--soft)}
.photo{box-shadow:0 4px 10px rgba(0,0,0,.18)}
.about-text{font-size:16px;line-height:26px;color:#333}
.t-name{font-size:15px;font-weight:500;text-transform:uppercase;width:300px;text-align:center}
.avatar{width:70px;height:70px;border-radius:50%;background:linear-gradient(#dfe4ea,#9fb0c2)}
.quote{width:26px;height:26px;border-radius:50%;background:#3a3a3a}
.stars{font-size:18px;letter-spacing:7px;color:var(--yellow);width:300px;text-align:center}
.t-text{width:330px;text-align:center;font-size:16px;line-height:26px;color:var(--muted)}
.blog{left:0;top:2101px;width:1200px;height:583px;background:var(--blog)}
.blog-img{width:296px;height:205px}
.date{width:37px;height:58px;border-radius:18px;background:var(--yellow);text-align:center;font-weight:500}
.date b{display:block;font-size:20px;margin-top:6px;font-weight:500}
.date i{display:block;font-style:normal;font-size:12px}
.post{width:269px;height:177px;background:var(--white);text-align:center}
.post h3{margin-top:30px;font-family:var(--serif);font-size:14px;line-height:19px;text-transform:uppercase;padding:0 20px}
.post p{margin-top:12px;font-size:16px;line-height:19px;color:var(--muted);padding:0 16px}
.post a{display:inline-flex;align-items:center;gap:12px;margin-top:12px;color:var(--yellow);font-weight:500;font-size:15px;text-decoration:none}
.footer{left:0;top:2684px;width:1200px;height:335px;background:var(--footer);color:var(--white)}
.f-head{font-size:15px;font-weight:700;text-transform:uppercase}
.f-links{list-style:none;font-size:16px;line-height:32.6px}
.f-circle{width:36px;height:36px;border-radius:50%;border:1px solid var(--white)}
</style>
</head>
<body>
<div class="abs topbar"></div>

<header class="abs nav">
  <a style="left:109px">Home</a>
  <a style="left:188px">About</a>
  <a style="left:272px">Reviews</a>
  <a style="left:370px">Benefit</a>
  <div class="brand">TARNWISP</div>
  <a style="left:733px">Why Choose Us</a>
  <a style="left:888px">Conact Us</a>
  <span class="social" style="left:1004px"></span>
  <span class="social" style="left:1040px"></span>
  <span class="social" style="left:1077px"></span>
</header>

<section class="abs hero" role="img" aria-label="Athlete tying her sneaker laces on a wooden basketball court beside a ball and water bottle"></section>
<h1 class="abs hero-title">TARNWISP</h1>
<p class="abs hero-text">Lorem ipsum dolor sit&nbsp; consectetur adipiscing elit, sed do eiusmod tempor incididunt ut labore.</p>
<div class="abs btn" style="left:737px;top:404px;width:158px;height:46px">Get Stared
  <svg viewBox="0 0 16 16"><circle cx="8" cy="8" r="8" fill="#111"/><path d="M4 8h7M8 5l3 3-3 3" stroke="#f5b000" stroke-width="2" fill="none"/></svg></div>
<div class="abs slider-btn" style="left:539px;top:565px;background:#fff"><svg width="16" height="10" viewBox="0 0 16 10"><path d="M15 5H2M6 1 2 5l4 4" stroke="#111" stroke-width="2" fill="none"/></svg></div>
<div class="abs" style="left:595px;top:573px;width:10px;height:10px;border-radius:50%;background:var(--yellow)"></div>
<div class="abs slider-btn" style="left:625px;top:565px;background:var(--yellow)"><svg width="16" height="10" viewBox="0 0 16 10"><path d="M1 5h13M10 1l4 4-4 4" stroke="#111" stroke-width="2" fill="none"/></svg></div>

<!-- Why choose us -->
<h2 class="abs h2" style="left:111px;top:710px">Why Choose Us</h2>
<div class="abs rule" style="left:111px;top:760px"></div>
<p class="abs body-grey" style="left:111px;top:791px;width:380px">Lorem ipsum dolor sit amet, consectetur adipiscing elit, sed do eiusmod tempor incididunt ut labore et dolore magna aliqua. Ut enim ad minim veniam, quis nostrud exercitation ullamco laboris nisi ut aliquip ex ea commodo consequatreprehenderit luptate velit</p>
<div class="abs btn" style="left:111px;top:952px;width:159px;height:46px">Learn More
  <svg viewBox="0 0 16 16"><circle cx="8" cy="8" r="8" fill="#111"/><path d="M4 8h7M8 5l3 3-3 3" stroke="#f5b000" stroke-width="2" fill="none"/></svg></div>

<div class="abs card" style="left:541px;top:718px"><svg width="64" height="66" viewBox="0 0 64 66"><path d="M6 2h22v34l30 10v14H6z" fill="#f5b000"/><rect x="6" y="58" width="52" height="6" fill="#f5b000"/></svg><span>Lorem ipsum dolor</span></div>
<div class="abs card active" style="left:728px;top:718px"><svg width="90" height="66" viewBox="0 0 90 66"><path d="M4 56V36q8-6 20-4l20-16 30 22q12 6 12 18z" fill="#f5b000"/><rect x="4" y="56" width="82" height="6" rx="3" fill="#f5b000"/></svg><span>Lorem ipsum dolor</span></div>
<div class="abs card" style="left:913px;top:718px"><svg width="62" height="66" viewBox="0 0 62 66"><rect x="2" y="2" width="26" height="62" rx="13" fill="#f5b000"/><rect x="34" y="2" width="26" height="62" rx="13" fill="#f5b000"/><path d="M2 24h26M2 34h26M34 24h26M34 34h26" stroke="#fff" stroke-width="4"/></svg><span>Lorem ipsum dolor</span></div>
<div class="abs card" style="left:541px;top:878px"><svg width="56" height="68" viewBox="0 0 56 68"><ellipse cx="15" cy="34" rx="13" ry="32" fill="#f5b000"/><ellipse cx="41" cy="34" rx="13" ry="32" fill="#f5b000"/><path d="M8 30l7-10 7 10M34 30l7-10 7 10" stroke="#fff" stroke-width="3" fill="none"/></svg><span>Lorem ipsum dolor</span></div>
<div class="abs card" style="left:728px;top:878px"><svg width="90" height="68" viewBox="0 0 90 68"><path d="M4 66V54q20-2 34-22L72 4h10l-4 62h-8l2-36L40 62H4z" fill="#f5b000"/></svg><span>Lorem ipsum dolor</span></div>
<div class="abs card" style="left:913px;top:878px"><svg width="104" height="64" viewBox="0 0 104 64"><path d="M4 54V12q10-8 24 0l16 14q30 4 52 16 6 4 6 12z" fill="#f5b000"/><rect x="4" y="54" width="98" height="8" rx="4" fill="#f5b000"/><path d="M40 40l10-12M52 42l10-12" stroke="#fff" stroke-width="4"/></svg><span>Lorem ipsum dolor</span></div>

<!-- About -->
<section class="abs about"></section>
<div class="abs photo" role="img" aria-label="Person in a blue cardigan sitting on a stool lacing up sneakers" style="left:109px;top:1159px;width:320px;height:281px;background:linear-gradient(135deg,#e8e2da,#8a9bc4 60%,#6f5a48)"></div>
<div class="abs photo" role="img" aria-label="Close-up of pink running shoes being laced on a yoga mat" style="left:321px;top:1306px;width:227px;height:181px;background:linear-gradient(135deg,#cfcfcf,#7a7a7a 55%,#e59aa2)"></div>
<div class="abs" style="left:334px;top:1316px;width:201px;height:162px;border:2px solid var(--yellow)"></div>
<svg class="abs" style="left:242px;top:1272px" width="56" height="56" viewBox="0 0 56 56"><circle cx="28" cy="28" r="27" fill="#fff"/><circle cx="28" cy="28" r="22" fill="none" stroke="#f5b000" stroke-width="4"/><path d="M23 19l14 9-14 9z" fill="#111"/></svg>

<h2 class="abs h2" style="left:620px;top:1150px">About Us</h2>
<div class="abs rule" style="left:620px;top:1200px"></div>
<p class="abs about-text" style="left:620px;top:1228px;width:470px">Lorem ipsum dolor sit amet, consectetur adipiscing elit,&nbsp; eiusmod tempor incididunt ut labore et dolore magna aliqua. Ut enim ad minim veniam, quis nostrud exercitation ullamco laboris nisi ut aliquip ex ea commodo consequat. Duis aute irure dolor in reprehen-derit in voluptate velit esse cillum dolore eu fugiat nulla pariatur. Excepteur sint occaecat cupidatat non proident, sunt in culpa qui officia deserunt mollit anim id est laborum.</p>
<div class="abs btn" style="left:620px;top:1440px;width:158px;height:46px">Learn More
  <svg viewBox="0 0 16 16"><circle cx="8" cy="8" r="8" fill="#111"/><path d="M4 8h7M8 5l3 3-3 3" stroke="#f5b000" stroke-width="2" fill="none"/></svg></div>

<!-- Testimonials -->
<h2 class="abs h2" style="left:0;width:1194px;text-align:center;top:1634px">Our Testimonials</h2>
<div class="abs rule" style="left:577px;top:1683px"></div>

<div class="abs t-name" style="left:238px;top:1762px">Owen Marlow</div>
<div class="abs avatar" role="img" aria-label="Reviewer portrait" style="left:351px;top:1794px"></div>
<div class="abs quote" style="left:420px;top:1827px"></div>
<div class="abs stars" style="left:249px;top:1882px">★★★★★</div>
<p class="abs t-text" style="left:234px;top:1915px">Lorem ipsum dolor consectetur adipiscing elit, sed do eiusmod tempor incididunt ut labore dolore magna aliqua.enim&nbsp; minim veniam exercitation commodo consequat.</p>

<div class="abs t-name" style="left:641px;top:1762px">Evan Pryce</div>
<div class="abs avatar" role="img" aria-label="Reviewer portrait" style="left:754px;top:1794px"></div>
<div class="abs quote" style="left:823px;top:1827px"></div>
<div class="abs stars" style="left:652px;top:1882px">★★★★<span style="color:#1f5fbf">★</span></div>
<p class="abs t-text" style="left:637px;top:1915px">Lorem ipsum dolor consectetur adipiscing elit, sed do eiusmod tempor incididunt ut labore dolore magna aliqua.enim&nbsp; minim veniam exercitation commodo consequat.</p>

<div class="abs slider-btn" style="left:146px;top:1895px;background:var(--yellow)"><svg width="16" height="10" viewBox="0 0 16 10"><path d="M15 5H2M6 1 2 5l4 4" stroke="#111" stroke-width="2" fill="none"/></svg></div>
<div class="abs slider-btn" style="left:1019px;top:1895px;background:var(--yellow)"><svg width="16" height="10" viewBox="0 0 16 10"><path d="M1 5h13M10 1l4 4-4 4" stroke="#111" stroke-width="2" fill="none"/></svg></div>

<!-- Blog -->
<section class="abs blog"></section>
<h2 class="abs h2" style="left:0;width:1204px;text-align:center;top:2150px;color:#fff">Our Blog</h2>
<div class="abs rule" style="left:584px;top:2202px;background:#fff"></div>

<div class="abs blog-img" role="img" aria-label="Pair of brown leather dress shoes" style="left:128px;top:2260px;background:linear-gradient(135deg,#6b4a30,#2a1c12)"></div>
<div class="abs blog-img" role="img" aria-label="Shoe factory worker holding a finished sneaker" style="left:454px;top:2260px;background:linear-gradient(135deg,#b9b3a8,#5e5852)"></div>
<div class="abs blog-img" role="img" aria-label="Smiling factory worker holding a pair of white sandals" style="left:779px;top:2260px;background:linear-gradient(135deg,#c9ccd2,#4b5d80)"></div>
<div class="abs date" style="left:145px;top:2274px"><b>5</b><i>Jul</i></div>
<div class="abs date" style="left:471px;top:2274px"><b>5</b><i>Jul</i></div>
<div class="abs date" style="left:796px;top:2274px"><b>5</b><i>Jul</i></div>

<article class="abs post" style="left:139px;top:2432px"><h3>Lorem ipsum consectetur adipiscing elit sed do</h3><p>Lorem ipsum dolor&nbsp; consectetur adipiscing elit, sed do eiusmod</p><a>READ MORE <svg width="15" height="15" viewBox="0 0 16 16"><circle cx="8" cy="8" r="8" fill="#f5b000"/><path d="M4 8h7M8 5l3 3-3 3" stroke="#fff" stroke-width="2" fill="none"/></svg></a></article>
<article class="abs post" style="left:465px;top:2432px"><h3>Lorem ipsum consectetur adipiscing elit sed do</h3><p>Lorem ipsum dolor&nbsp; consectetur adipiscing elit, sed do eiusmod</p><a>READ MORE <svg width="15" height="15" viewBox="0 0 16 16"><circle cx="8" cy="8" r="8" fill="#f5b000"/><path d="M4 8h7M8 5l3 3-3 3" stroke="#fff" stroke-width="2" fill="none"/></svg></a></article>
<article class="abs post" style="left:791px;top:2432px"><h3>Lorem ipsum consectetur adipiscing elit sed do</h3><p>Lorem ipsum dolor&nbsp; consectetur adipiscing elit, sed do eiusmod</p><a>READ MORE <svg width="15" height="15" viewBox="0 0 16 16"><circle cx="8" cy="8" r="8" fill="#f5b000"/><path d="M4 8h7M8 5l3 3-3 3" stroke="#fff" stroke-width="2" fill="none"/></svg></a></article>

<!-- Footer -->
<footer class="abs footer">
  <div class="abs brand" style="left:111px;top:30px;font-size:40px;color:#fff">TARNWISP</div>
  <p class="abs" style="left:111px;top:91px;width:320px;font-size:16px;line-height:26px">Lorem ipsum dolor sit amet, consectetur adipiscing elit sed eiusmod tempor aliqua.</p>
  <div class="abs f-circle" style="left:111px;top:164px"></div>
  <div class="abs f-circle" style="left:153px;top:164px"></div>
  <div class="abs f-circle" style="left:194px;top:164px"></div>

  <div class="abs f-head" style="left:488px;top:38px">Quick Links</div>
  <ul class="abs f-links" style="left:488px;top:60px"><li>Home</li><li>About Us</li><li>Benefit</li><li>Reviews</li><li>Why Choose Us</li><li>Contact Us</li></ul>

  <div class="abs f-head" style="left:677px;top:38px">Other Links</div>
  <ul class="abs f-links" style="left:677px;top:60px"><li>Terms</li><li>Privacy</li><li>Policy</li><li>Services</li><li>FAQ</li></ul>

  <div class="abs f-head" style="left:846px;top:38px">Subscribe Newsletter</div>
  <p class="abs" style="left:846px;top:68px;width:250px;font-size:16px;line-height:23px">Lorem ipsum dolor&nbsp; consectetur adipiscing elit, sed do eiusmod tempor incididunt .</p>
  <div class="abs" style="left:846px;top:156px;width:209px;height:36px;background:#fff;border-radius:2px;color:#111;font-size:14px;padding:9px 0 0 14px">Enter your Email
    <svg class="abs" style="right:14px;top:13px" width="16" height="11" viewBox="0 0 16 11"><rect width="16" height="11" fill="#f5b000"/><path d="M0 0l8 6 8-6" stroke="#fff" stroke-width="1.5" fill="none"/></svg></div>

  <div class="abs" style="left:111px;top:275px;width:978px;height:1px;background:#555"></div>
  <p class="abs" style="left:0;width:1200px;text-align:center;top:295px;font-size:16px">©Copyright 2021 TarnWisp.&nbsp;&nbsp; All right reserved.</p>
</footer>
</body>
</html>
```